business card with logo

Would like a business card for an electrical contractor called BRANLOCK ELECTRICS.
No generic electrical imagery (light globe, powerpoints, ect). Would like a logo or symbol created in the design as part of the project . I would like crisp colour. No templated designs like Printvox

is there any other designers willing to submit designs

Electrical

```html
<!DOCTYPE html>
<html lang="en">
<head>
<meta charset="utf-8">
<title>Branlock Electrics – Business Card</title>
<link href="https://fonts.googleapis.com/css2?family=Open+Sans:wght@400;600;700&display=swap" rel="stylesheet">
<style>
  :root {
    --bg: #e9e9e9;
    --green: #1aa843;
    --green-line: #5aa832;
    --navy: #1c3d73;
    --ink: #3b3b3b;
    --card-white: #ffffff;
    --faint: #ececec;
  }
  * { box-sizing: border-box; margin: 0; padding: 0; }
  html, body {
    width: 1200px; height: 1200px; overflow: hidden;
    background: var(--bg);
    font-family: "Open Sans", Arial, sans-serif;
  }
  .sheet {
    width: 1200px; height: 1200px;
    display: flex; flex-direction: column;
    align-items: center; justify-content: center; gap: 60px;
  }
  .card {
    position: relative;
    width: 700px; height: 400px;
    overflow: hidden;
    box-shadow: 0 6px 18px rgba(0,0,0,0.12);
  }

  /* Front */
  .card--front { background: var(--green); }
  .card--front .brand {
    position: absolute; left: 50%; top: 50%;
    transform: translate(-50%, -50%);
  }

  /* Brand lockup */
  .brand { display: flex; align-items: center; gap: 14px; white-space: nowrap; }
  .brand__dot {
    width: 34px; height: 34px; border-radius: 50%;
    background: var(--navy);
    flex: none;
  }
  .brand__name {
    font-weight: 700; font-size: 40px; letter-spacing: 1px;
    color: var(--navy);
  }

  /* Back */
  .card--back { background: var(--card-white); }
  .card--back .brand {
    position: absolute; left: 150px; top: 62px;
  }
  .card--back .brand__dot { width: 26px; height: 26px; background: var(--green); }
  .card--back .brand__name { font-size: 32px; }

  .watermark {
    position: absolute; right: -40px; top: 110px;
    width: 220px; height: 220px; border-radius: 50%;
    background: var(--faint);
  }
  .divider {
    position: absolute; left: 300px; top: 130px;
    width: 1px; height: 110px; background: #bdbdbd;
  }
  .person {
    position: absolute; left: 70px; top: 150px;
    line-height: 1.25;
  }
  .person__name { font-size: 20px; font-weight: 600; color: var(--navy); }
  .person__licence { font-size: 18px; color: var(--ink); }
  .contact {
    position: absolute; left: 330px; top: 230px;
    display: flex; align-items: center; gap: 10px;
    font-size: 19px; color: var(--ink);
  }
  .contact svg { width: 20px; height: 20px; flex: none; }
  .band {
    position: absolute; left: 0; right: 0; bottom: 0; height: 44px;
    background: var(--navy);
    border-top: 4px solid var(--green-line);
  }
</style>
</head>
<body>
<main class="sheet">
  <section class="card card--front" aria-label="Card front">
    <div class="brand">
      <span class="brand__dot"></span>
      <span class="brand__name">BRANLOCK ELECTRICS</span>
    </div>
  </section>

  <section class="card card--back" aria-label="Card back">
    <div class="watermark"></div>
    <div class="brand">
      <span class="brand__dot"></span>
      <span class="brand__name">BRANLOCK ELECTRICS</span>
    </div>
    <div class="divider"></div>
    <div class="person">
      <p class="person__name">Owen Branlock</p>
      <p class="person__licence">Rec#40318</p>
    </div>
    <div class="contact">
      <svg viewBox="0 0 20 20" aria-hidden="true">
        <rect x="0" y="0" width="20" height="20" rx="4" fill="#1c3d73"/>
        <rect x="4" y="6" width="12" height="8" fill="none" stroke="#fff" stroke-width="1.4"/>
        <path d="M4 6 L10 11 L16 6" fill="none" stroke="#fff" stroke-width="1.4"/>
      </svg>
      <span>branlockelec@voltmail.com</span>
    </div>
    <div class="band"></div>
  </section>
</main>
</body>
</html>
```